Kindle Vine Path

I am developing a simple blog site that is focused on Catholic religion and I will write reflections on the New Testament Gospels daily. The focus is on how we Kindle Vine Path in our daily lives. The attached is showing a potential theme. The Eucharist in the Monstrance is shining out Jesus' light and love upon the fig tree and a community of people serving and helping each other. Building the kingdom of heaven on earth.

```html
<!DOCTYPE html>
<html lang="en">
<head>
<meta charset="utf-8">
<title>Kindle Vine Path</title>
<link rel="stylesheet" href="https://fonts.googleapis.com/css2?family=Figtree:wght@400;500;600&family=Libre+Baskerville:wght@400;700&display=swap">
<style>
:root{
  --teal:#0e3a4b;
  --navy:#1b212b;
  --cream:#efe6d6;
  --cyan:#00b4d8;
  --ink:#1f2430;
  --grey:#a9a9a9;
  --white:#ffffff;
}
*{margin:0;padding:0;box-sizing:border-box}
html,body{width:1200px;height:2818px;overflow:hidden}
body{position:relative;font-family:"Figtree",sans-serif;color:var(--ink);background:var(--white)}
.serif{font-family:"Libre Baskerville",serif}
section,header,footer{position:absolute;left:0;width:1200px}
.abs{position:absolute}

.topbar{top:0;height:25px;background:var(--teal);color:var(--white);font-size:9px;text-align:center;line-height:25px}
.topbar a{color:var(--cyan);text-decoration:none}

.hero{top:25px;height:306px;background:radial-gradient(circle at 50% 38%,#fbe3a8 0,#f3b866 18%,#e59a3d 45%,#c9742a 75%,#a95a22 100%)}
.hero-art{left:0;top:0;width:1200px;height:306px}
.nav{top:0;left:0;width:1200px;height:63px;background:rgba(58,44,32,.78);color:var(--white)}
.brand{left:180px;top:22px;font-size:14px;font-weight:600;letter-spacing:.2px}
.menu{right:180px;top:24px;display:flex;gap:27px;font-size:10px}
.menu .active{color:var(--cyan)}

.intro{top:331px;height:236px;text-align:center}
.intro .kicker{top:48px;width:100%;font-size:14px;letter-spacing:.2px}
.intro .intro-title{top:72px;width:100%;font-size:52px;font-weight:700;color:var(--ink)}
.btn-solid{background:var(--cyan);color:var(--white);font-size:9px;font-weight:600;text-align:center;border-radius:2px;text-transform:uppercase}
.intro .btn-solid{left:544px;top:159px;width:112px;height:26px;line-height:26px}

.featured{top:567px;height:423px;background:var(--cream);overflow:hidden}
.feat-glow{left:0;top:0;width:1200px;height:423px;background:linear-gradient(90deg,#5d6a5a 0,rgba(239,230,214,0) 28%),linear-gradient(270deg,#d8cdb8 0,rgba(239,230,214,0) 22%)}
.feat-photo{left:65px;top:54px;width:416px;height:369px;background:linear-gradient(180deg,#d7e0e6 0,#c4ccd1 45%,#8c8f8f 75%,#e9e0cf 100%)}
.feat-date{left:600px;top:131px;font-size:10px}
.feat-title{left:600px;top:152px;font-size:28px;line-height:50px;font-weight:700}
.btn-line{border:1px solid currentColor;font-size:9.5px;font-weight:600;text-align:center}
.featured .btn-line{left:600px;top:262px;width:110px;height:28px;line-height:26px}

.posts{top:990px;height:966px;background:var(--navy);color:var(--white)}
.posts .posts-title{top:60px;width:100%;text-align:center;font-size:21px;font-weight:700}
.posts .sub{top:102px;width:100%;text-align:center;font-size:9px}
.posts .sub span{color:var(--cyan)}
.card{background:var(--cream);color:var(--ink)}
.card .pic{left:0;top:0;width:100%;height:152px;background:var(--grey)}
.card .tag{left:21px;top:143px;height:17px;padding:0 10px;line-height:17px;background:var(--cyan);color:var(--white);font-size:8.5px;font-weight:600;border-radius:2px}
.card .card-title{left:19px;top:174px;right:19px;font-size:14.5px;font-weight:400;line-height:22px}
.card .excerpt{left:19px;right:19px;font-size:8px;line-height:15px}
.card .more{left:19px;font-size:8.5px;font-weight:600}
.wide .excerpt{top:210px}
.wide .more{top:286px}
.narrow .excerpt{top:230px}
.narrow .more{top:295px}
.posts .btn-line{left:546px;top:876px;width:108px;height:27px;line-height:25px;color:var(--white)}

.community{top:1956px;height:700px}
.community .community-title{left:180px;top:59px;font-size:27px;font-weight:700}
.community .crowd{left:180px;top:126px;width:383px;height:172px;background:linear-gradient(90deg,#c98a6e,#e8b67a 25%,#7a6d92 50%,#d98b6a 70%,#b8a3d8 100%);opacity:.85}
.community .quote-card{left:613px;top:62px;width:406px;height:237px;background:var(--cream);border-radius:14px}
.quote-card .mark{left:22px;top:-14px;font-size:120px;color:#c7bfb1;line-height:1}
.quote-card .words{left:65px;top:62px;font-size:22px;font-weight:700;line-height:38px}
.community .fig-title{left:180px;top:369px;font-size:27px;font-weight:700}
.community .fig-text{left:181px;top:432px;width:215px;font-size:9.5px;line-height:18.5px}
.community .btn-solid{left:181px;top:592px;width:87px;height:26px;line-height:26px}
.community .art-a{left:464px;top:374px;width:247px;height:127px;background:linear-gradient(135deg,#2f4a8c,#5a77b8 40%,#a8824e 65%,#3a5796)}
.community .art-b{left:464px;top:519px;width:247px;height:118px;background:linear-gradient(180deg,#b6c3cc,#9c8a6a 50%,#7a5c3c)}
.community .art-c{left:733px;top:374px;width:284px;height:263px;background:linear-gradient(160deg,#a9d0e6,#7fb4d8 45%,#5c8f5a 75%,#9fc6e0)}

.scripture{top:2656px;height:106px;background:var(--teal);color:var(--white)}
.scripture .scripture-title{left:386px;top:37px;font-size:27px;font-weight:700}
.scripture .btn-solid{left:713px;top:40px;width:100px;height:27px;line-height:27px}

.footer{top:2762px;height:56px;background:var(--navy);color:var(--white);font-size:8.5px;text-align:center;line-height:56px}
</style>
</head>
<body>

<div class="topbar">How we Kindle Vine Path in our daily lives? <a>Subscribe Now!</a></div>

<header class="hero">
  <svg class="abs hero-art" role="img" aria-label="Golden monstrance radiating rays of light over a warm orange sky" viewBox="0 0 1200 306">
    <defs>
      <radialGradient id="halo" cx="50%" cy="50%" r="50%">
        <stop offset="0" stop-color="#fff3d6" stop-opacity=".55"/>
        <stop offset="1" stop-color="#fff3d6" stop-opacity="0"/>
      </radialGradient>
    </defs>
    <circle cx="600" cy="180" r="105" fill="url(#halo)"/>
    <rect x="584" y="120" width="32" height="165" rx="10" fill="#d89a2c" opacity=".5"/>
  </svg>
  <nav class="abs nav">
    <div class="abs brand">KINDLE VINE PATH</div>
    <div class="abs menu"><span>Home</span><span class="active">About</span><span>Eucharist</span><span>Community</span><span>Resources</span><span>Contact</span></div>
  </nav>
</header>

<section class="intro">
  <div class="abs kicker">HOW WE KINDLE VINE PATH IN OUR DAILY LIVES?</div>
  <h1 class="abs intro-title serif">Kindle Vine Path</h1>
  <div class="abs btn-solid">Join us today!</div>
</section>

<section class="featured">
  <div class="abs feat-glow"></div>
  <div class="abs feat-photo" role="img" aria-label="Photograph of a white church bell tower with domes and a cross against a pale sky"></div>
  <div class="abs feat-date">03 MAY 2025</div>
  <div class="abs feat-title serif">Best Featured Post<br>Of The Week</div>
  <div class="abs btn-line">Continue Reading</div>
</section>

<section class="posts">
  <h2 class="abs posts-title serif">Check Our Latest Weekly Posts</h2>
  <div class="abs sub"><span>Subscribe</span> to get the latest content sent straight to your inbox.</div>

  <article class="abs card wide" style="left:180px;top:160px;width:410px;height:318px">
    <div class="abs pic" role="img" aria-label="Post image"></div>
    <div class="abs tag">03 MAY 2025</div>
    <h3 class="abs card-title serif">Pork belly palo santo cardigan you probably</h3>
    <p class="abs excerpt">Typewriter vaporware readymade pug aesthetic. Pork belly palo santo cardigan you probably haven't heard of them, meh street art af roof party mlkshk trust fund lo-fi. Small batch skate-board copper mug food truck taxidermy 8-bit hot chicken organic lumbersexual, put a bird on it kombucha live-edge.</p>
    <div class="abs more">Continue Reading...</div>
  </article>
  <article class="abs card wide" style="left:609px;top:160px;width:410px;height:318px">
    <div class="abs pic" role="img" aria-label="Post image"></div>
    <div class="abs tag">03 MAY 2025</div>
    <h3 class="abs card-title serif">Pork belly palo santo cardigan you probably</h3>
    <p class="abs excerpt">Typewriter vaporware readymade pug aesthetic. Pork belly palo santo cardigan you probably haven't heard of them, meh street art af roof party mlkshk trust fund lo-fi. Small batch skate-board copper mug food truck taxidermy 8-bit hot chicken organic lumbersexual, put a bird on it kombucha live-edge.</p>
    <div class="abs more">Continue Reading...</div>
  </article>

  <article class="abs card narrow" style="left:180px;top:498px;width:266px;height:340px">
    <div class="abs pic" role="img" aria-label="Post image"></div>
    <div class="abs tag">03 MAY 2025</div>
    <h3 class="abs card-title serif">Pork belly palo santo cardigan you probably</h3>
    <p class="abs excerpt">Typewriter vaporware readymade pug aesthetic. Pork belly palo santo cardigan you probably haven't heard of them, meh street art af roof party mlkshk trust fund lo-fi. Small batch skate-board copper mug food truck taxidermy live-edge.</p>
    <div class="abs more">Continue Reading...</div>
  </article>
  <article class="abs card narrow" style="left:467px;top:498px;width:266px;height:340px">
    <div class="abs pic" role="img" aria-label="Post image"></div>
    <div class="abs tag">03 MAY 2025</div>
    <h3 class="abs card-title serif">Pork belly palo santo cardigan you probably</h3>
    <p class="abs excerpt">Typewriter vaporware readymade pug aesthetic. Pork belly palo santo cardigan you probably haven't heard of them, meh street art af roof party mlkshk trust fund lo-fi. Small batch skate-board copper mug food truck taxidermy live-edge.</p>
    <div class="abs more">Continue Reading...</div>
  </article>
  <article class="abs card narrow" style="left:753px;top:498px;width:266px;height:340px">
    <div class="abs pic" role="img" aria-label="Post image"></div>
    <div class="abs tag">03 MAY 2025</div>
    <h3 class="abs card-title serif">Pork belly palo santo cardigan you probably</h3>
    <p class="abs excerpt">Typewriter vaporware readymade pug aesthetic. Pork belly palo santo cardigan you probably haven't heard of them, meh street art af roof party mlkshk trust fund lo-fi. Small batch skate-board copper mug food truck taxidermy live-edge.</p>
    <div class="abs more">Continue Reading...</div>
  </article>

  <div class="abs btn-line">View All Posts</div>
</section>

<section class="community">
  <h2 class="abs community-title serif">Community</h2>
  <div class="abs crowd" role="img" aria-label="Illustration of a diverse group of families and neighbours walking together"></div>
  <div class="abs quote-card">
    <div class="abs mark serif" aria-hidden="true">&ldquo;</div>
    <div class="abs words serif">&ldquo; Reflections on the<br>New Testament Gospels<br>Daily Lives &rdquo;</div>
  </div>

  <h2 class="abs fig-title serif">The Fig Tree</h2>
  <p class="abs fig-text">Typewriter vaporware readymade pug aesthet-ic. Pork belly palo santo cardigan you probably haven't heard of them, meh street art af roof party mlkshk trust fund lo-fi. Small batch skateboard copper mug food truck taxidermy 8-bit hot chicken organic lumbersexual, put a bird on it kombucha live-edge.</p>
  <div class="abs btn-solid">Read more</div>

  <div class="abs art-a" role="img" aria-label="Mosaic-style painting of the crucifixion under a blue sky"></div>
  <div class="abs art-b" role="img" aria-label="Mosaic-style painting of a bare fig tree with figures in a landscape"></div>
  <div class="abs art-c" role="img" aria-label="Mosaic-style painting of a fig branch with ripe figs and leaves against blue sky"></div>
</section>

<section class="scripture">
  <h2 class="abs scripture-title serif">Quote or Scripture</h2>
  <div class="abs btn-solid">Donate now</div>
</section>

<footer class="footer">&copy; Organization Name 2025. All Rights Reserved</footer>

</body>
</html>
```